Creation of a construction/bricklaying business website

Following the template format of "Wendmoor 2", the following content would need to be included:
1. Landing page with 3 tiles that go to their own pages.
- Landing page to include background photo and description of services offered.
2. 3 tiles to include:
a) "Contact Us For A Free Quote or Friendly Discussion" Form (middle tile)
b) Case Studies and Testimonials
c) Certifications and Professional Membership
- Design logo to be used from previous PixelHarbor project. Example of logo attached below, please access full JPG files from our account.

Target Market(s)

Prospective clients seeking construction work (bricklaying speciality)

Industry/Entity Type

Residential Construction

Coding

Coded - Design and coding required

Number of Pages Required

4 page

Font styles to use
Sans Serif

Colors

Designer to choose colors to be used in the design.

Requirements
Must have
• Following the template format of "Wendmoor 2", the following content would need to be included:
• 1. Landing parent page with 3 tiles that go to the 3 child pages.
• - Landing page to include background photo and description of services offered.
• 2. 3 tiles to include:
• a) "Contact Us For A Free Quote or Friendly Discussion" Form (middle tile)
• b) Case Studies and Testimonials (first tile / left side)
• c) Certifications and Professional Memberships (third tile / right side) (This should include logos of the relevant organisations being displayed. Specifically QLT and the Keystone Pact QLT).
• - Design logo to be used from previous PixelHarbor project. Example of logo attached below, please access full JPG files from our account.
Nice to have
• Sleek and modern feel.
• Approachable in terms of how people can contact the company for a quote.
• Traditional pictures to give credibility and comfort around choosing this company.
Should not have
• Cheesy pictures
• Over-complicated
• Simple to use
• Easy URL domain name

```html
<!DOCTYPE html>
<html lang="en">
<head>
<meta charset="utf-8">
<title>R.T.Hale Construction Ltd</title>
<link rel="stylesheet" href="https://fonts.googleapis.com/css2?family=Arimo:wght@400;500;700&family=Nunito+Sans:wght@300;400;600&display=swap">
<style>
:root{
  --blue:#1559a6;
  --bar:#6a6a6a;
  --tile:#e8ecec;
  --field:#edf1f1;
  --btn:#5b5b5b;
  --ink:#1d1d1d;
  --white:#ffffff;
}
*{margin:0;padding:0;box-sizing:border-box}
html,body{width:972px;height:1200px;overflow:hidden;background:var(--white)}
body{position:relative;font-family:"Nunito Sans",sans-serif;color:var(--ink)}
.abs{position:absolute}
/* header */
.topbar{left:0;top:0;width:972px;height:31px}
.contact-top{top:6px;display:flex;align-items:center;gap:8px;color:var(--white);font-family:"Arimo",sans-serif;font-size:13px}
.ico-circle{width:20px;height:20px;border-radius:50%;background:var(--blue);display:flex;align-items:center;justify-content:center}
.brand{left:130px;top:22px;color:var(--blue);font-family:"Arimo",sans-serif;font-weight:700;line-height:1}
.brand .name{font-size:30px;display:flex;align-items:center;gap:6px}
.brand .mark{width:10px;height:10px;background:var(--blue)}
.brand .sub{font-size:11px;letter-spacing:2px;margin-top:4px}
.nav{top:55px;font-family:"Arimo",sans-serif;font-size:11.5px;text-align:center;line-height:15px;color:#333}
/* hero */
.hero{left:0;top:98px;width:972px;height:425px;background:linear-gradient(180deg,#9dc1de 0%,#b7cbd8 22%,#8a5a44 45%,#7b6a5a 68%,#6a8a3e 80%,#8a7f78 100%)}
.hero-card{left:120px;top:202px;width:270px;height:168px;background:rgba(30,30,30,.72);color:var(--white);font-family:"Arimo",sans-serif;padding:9px 17px}
.hero-card p{font-size:12px;line-height:15px;font-weight:500}
.services{display:grid;grid-template-columns:136px 120px;row-gap:10px;margin-top:12px}
.services li{list-style:none;display:flex;align-items:center;gap:11px;font-size:13.5px;line-height:16px}
.dot{width:12px;height:12px;border-radius:50%;background:#ddeeff;border:2px solid var(--blue);flex:none}
/* about */
.about-title{left:0;width:972px;top:550px;text-align:center;color:var(--blue);font-family:"Arimo",sans-serif;font-weight:700;font-size:22px}
.about-text{left:130px;width:712px;top:588px;text-align:center;font-size:12.5px;line-height:19.5px}
.about-text p+p{margin-top:13px}
/* tiles */
.tile{top:709px;width:231px;height:246px;background:var(--tile)}
.tile-head{height:35px;background:var(--blue);color:var(--white);font-family:"Arimo",sans-serif;font-size:11.5px;line-height:15px;font-weight:500;display:flex;align-items:center;padding-left:60px;position:relative}
.tile-head svg{position:absolute;left:10px;top:4px}
.btn{position:absolute;bottom:11px;background:var(--btn);color:var(--white);font-family:"Arimo",sans-serif;font-size:11.5px;font-weight:500;padding:4px 13px}
.quote{position:absolute;left:7px;top:43px;width:215px;height:108px;background:var(--field);border-radius:6px;font-size:9.5px;line-height:15.5px;padding:8px 12px 0 16px}
.quote::before{content:"\201C";position:absolute;left:13px;top:2px;font-size:26px;color:#bcc;font-family:Georgia,serif}
.quote span{padding-left:15px}
.avatar{position:absolute;left:21px;top:140px;width:52px;height:52px;border-radius:50%;background:linear-gradient(135deg,#c7a184,#8b5a3e);border:3px solid var(--white);box-shadow:0 0 2px #999}
.client{position:absolute;left:83px;top:177px;font-size:9px;font-weight:600}
.field{position:absolute;left:11px;width:209px;height:25px;background:var(--field);border:1px solid #d9dfdf;font-size:10.5px;display:flex;align-items:center;gap:9px;padding-left:9px}
.certs-text{position:absolute;left:0;width:231px;top:44px;text-align:center;font-size:11px;line-height:18px}
/* footer */
.footer{left:0;top:997px;width:972px;height:203px;background:linear-gradient(180deg,#3c4a55 0%,#4d5a4f 45%,#3d5a2c 75%,#2f4a22 100%)}
.footer-shade{left:0;top:997px;width:972px;height:203px;background:rgba(20,25,30,.45)}
.footer-brand{left:0;width:972px;top:1037px;text-align:center;color:var(--white);font-family:"Arimo",sans-serif;font-weight:700;line-height:1}
.footer-item{top:1080px;display:flex;align-items:center;gap:14px;color:var(--white);font-size:11.5px;font-weight:300;line-height:18px}
.footer-item .ico-circle{width:31px;height:31px}
.copyright{left:150px;top:1166px;color:var(--white);font-size:11.5px;font-weight:300}
.social{left:696px;top:1159px;display:flex;gap:4px}
.social span{width:25px;height:25px;border-radius:50%;background:var(--white);display:block}
</style>
</head>
<body>

<header>
  <svg class="abs topbar" width="972" height="31" aria-hidden="true"><polygon points="413,0 972,0 972,31 453,31" fill="#6a6a6a"/><line x1="0" y1="1" x2="413" y2="1" stroke="#6a6a6a" stroke-width="2"/></svg>
  <div class="abs contact-top" style="left:484px">
    <span class="ico-circle"><svg width="11" height="8"><rect x=".5" y=".5" width="10" height="7" fill="#fff"/><polyline points=".5,.5 5.5,4.5 10.5,.5" fill="none" stroke="#1559a6"/></svg></span>
    info@rthalebuild.com
  </div>
  <div class="abs contact-top" style="left:720px;font-size:14px">
    <span class="ico-circle"><svg width="10" height="10"><path d="M2 0 L4 2.5 L3 4 Q4.5 6 6 7 L7.5 6 L10 8 L8.5 10 Q3 9 0 2 Z" fill="#fff"/></svg></span>
    555.014.2290
  </div>
  <div class="abs brand">
    <div class="name"><span class="mark"></span>R.T.Hale</div>
    <div class="sub">CONSTRUCTION LTD</div>
  </div>
  <nav>
    <div class="abs nav" style="left:432px;width:104px">Case Studies and<br>Testimonials</div>
    <div class="abs nav" style="left:553px;width:108px">Contact Us For A<br>Free Quote</div>
    <div class="abs nav" style="left:680px;width:176px;top:53px">Certifications and Professional<br>Memberships</div>
  </nav>
</header>

<section class="abs hero" role="img" aria-label="Photo of red brick detached houses with gravel front gardens on a sunny residential street"></section>
<div class="abs hero-card">
  <p>R.T.Hale Construction Ltd is a construction company that has expertise and experience in the following areas</p>
  <ul class="services">
    <li><span class="dot"></span>Extensions</li>
    <li><span class="dot"></span>Garden walls</li>
    <li><span class="dot"></span>New build /<br>New houses</li>
    <li><span class="dot"></span>Plastering</li>
    <li><span class="dot"></span>Garden walls</li>
    <li><span class="dot"></span>Brickwork</li>
  </ul>
</div>

<h1 class="abs about-title">About Us</h1>
<div class="abs about-text">
  <p>We pride ourselves on attention to detail, pride in our completed project and client satisfaction. We believe in full transparency and this is reflected in the jobs we quote for you. We break down each step with both labour and materials cost so you can see exactly what you are paying for.</p>
  <p>Feel free to get in touch and we can talk through what you are looking to achieve.</p>
</div>

<section class="abs tile" style="left:130px">
  <div class="tile-head">
    <svg width="42" height="28" aria-hidden="true"><rect x="14" y="2" width="20" height="24" rx="2" fill="none" stroke="#fff" stroke-width="1.5"/><line x1="18" y1="9" x2="30" y2="9" stroke="#fff"/><line x1="18" y1="13" x2="27" y2="13" stroke="#fff"/><circle cx="28" cy="19" r="4" fill="none" stroke="#fff" stroke-width="1.5"/><ellipse cx="8" cy="20" rx="7" ry="5" fill="#fff"/></svg>
    Case Studies and<br>Testimonials
  </div>
  <div class="quote"><span></span>Lorem ipsum dolor sit amet conetuge sed diay nibhdl tincidunt ut laoreet dolore magam er vol wisi enim ad minim vni quis nostrud exerci tationorem ipsum dolor sit ametee sed diammmy nibh.</div>
  <div class="avatar" role="img" aria-label="Client portrait photo"></div>
  <div class="client">Mr.Owen Preston</div>
  <span class="btn" style="left:6px">View All</span>
</section>

<section class="abs tile" style="left:370px">
  <div class="tile-head" style="padding-left:46px">
    <svg width="30" height="28" aria-hidden="true"><rect x="3" y="2" width="20" height="24" rx="2" fill="none" stroke="#fff" stroke-width="1.5"/><line x1="7" y1="9" x2="19" y2="9" stroke="#fff"/><line x1="7" y1="13" x2="15" y2="13" stroke="#fff"/><line x1="12" y1="22" x2="26" y2="8" stroke="#fff" stroke-width="2.5"/></svg>
    Contact Us For A<br>Free Quote
  </div>
  <div class="field" style="top:43px"><svg width="10" height="10"><circle cx="5" cy="3" r="2.8" fill="#1559a6"/><path d="M0 10 Q5 3 10 10Z" fill="#1559a6"/></svg>Your Name</div>
  <div class="field" style="top:74px"><svg width="11" height="8"><rect x=".5" y=".5" width="10" height="7" fill="#1559a6"/><polyline points=".5,.5 5.5,4.5 10.5,.5" fill="none" stroke="#fff"/></svg>Email Address</div>
  <div class="field" style="top:104px"><svg width="10" height="10"><path d="M2 0 L4 2.5 L3 4 Q4.5 6 6 7 L7.5 6 L10 8 L8.5 10 Q3 9 0 2 Z" fill="#1559a6"/></svg>Phone</div>
  <div class="field" style="top:134px;height:65px;align-items:flex-start;padding-top:5px"><svg width="11" height="11"><polygon points="0,5 11,0 7,11 5,6" fill="#1559a6"/></svg>Message</div>
  <span class="btn" style="left:11px;padding:4px 19px">Submit</span>
</section>

<section class="abs tile" style="left:610px">
  <div class="tile-head" style="padding-left:46px">
    <svg width="28" height="28" aria-hidden="true"><rect x="4" y="2" width="18" height="24" rx="2" fill="none" stroke="#fff" stroke-width="1.5"/><circle cx="13" cy="10" r="3" fill="#fff"/><line x1="8" y1="17" x2="18" y2="17" stroke="#fff"/><line x1="8" y1="21" x2="18" y2="21" stroke="#fff"/></svg>
    Certifications and Professional<br>Memberships
  </div>
  <div class="certs-text">Ut wisi enim ad minim veniam, quis nostrud<br>exerci tation ullamcorper suscipit.</div>
  <svg class="abs" style="left:20px;top:94px" width="200" height="90" role="img" aria-label="Membership badges: QLT and Keystone Pact QLT">
    <rect x="0" y="0" width="52" height="86" rx="3" fill="#c4122f"/>
    <rect x="60" y="11" width="40" height="70" fill="#b3162a"/>
    <rect x="111" y="12" width="77" height="38" fill="#d52b1e"/>
    <rect x="113" y="14" width="73" height="34" fill="#fff"/>
    <rect x="111" y="61" width="77" height="12" fill="#c6c6c6"/>
  </svg>
  <span class="btn" style="left:14px;padding:4px 4px">Know More</span>
</section>

<footer>
  <div class="abs footer" role="img" aria-label="Photo of a new-build housing development with trees and a lawn"></div>
  <div class="abs footer-shade"></div>
  <div class="abs footer-brand"><div style="font-size:20px">R.T.Hale</div><div style="font-size:8px;letter-spacing:1.5px;margin-top:3px">CONSTRUCTION LTD</div></div>
  <div class="abs footer-item" style="left:150px">
    <span class="ico-circle"><svg width="12" height="16"><path d="M6 16 L1 7 A5.5 5.5 0 1 1 11 7 Z" fill="#fff"/><circle cx="6" cy="5.5" r="2" fill="#1559a6"/></svg></span>
    <div>Street Name, City Name<br>State Zipcode</div>
  </div>
  <div class="abs footer-item" style="left:410px">
    <span class="ico-circle"><svg width="14" height="14"><path d="M3 0 L6 3.5 L4.5 5.5 Q6.5 8.5 8.5 9.5 L10.5 8 L14 11 L12 14 Q4 13 0 3 Z" fill="#fff"/></svg></span>
    <div>Call Us On :<br>555.014.2290</div>
  </div>
  <div class="abs footer-item" style="left:626px">
    <span class="ico-circle"><svg width="16" height="11"><rect x=".5" y=".5" width="15" height="10" fill="#fff"/><polyline points=".5,.5 8,6 15.5,.5" fill="none" stroke="#1559a6"/></svg></span>
    <div>Email<br>info@rthalebuild.com</div>
  </div>
  <div class="abs copyright">Copyright ©2018 R.T.Hale Construction Ltd. All Rights Reserved.</div>
  <div class="abs social" aria-label="Social links"><span></span><span></span><span></span><span></span></div>
</footer>

</body>
</html>
```